KLR Lending Website

Need a web site designed for a Professional Mortgage company along the lines of the draft site www.klrlending-demo.com.au

The main purpose of the site is to provide a professional image of the company and capture email address's and send out simple messages. ie "INTEREST RATE SPECIAL 4.5% FOR THE MONTH OF JUNE" or whatever...basically short punchy messages to hook people.

The content is important but a lot of that can be provided by links to our lender panel, several of which have been set up.

Most people will want to know current interest rates, and how much they can borrow along with what it will cost. There are various calculators embedded in the lenders sites such as "Repayment Calculators" Borrow Capacity Calculators" Stamp Duty Calculators"

These would be nice to have on site, but if to costly or difficult to start the links can suffice.

The site will need to be updated/amended regularily.

Example "Interest Rate Special" or "Current Special Offer" sections would be required and would need to be easyily editable and in fact would need to be able to switch them off if there is no special running.

Target Market(s)

Target market is a broad spectrum of people from young couple buying first home to older couples investing.

Industry/Entity Type

It Company

Requirements
Must have
• email capture, preferably need to enter email to enter site.

```html
<!DOCTYPE html>
<html lang="en">
<head>
<meta charset="utf-8">
<title>KLR Lending Services</title>
<link href="https://fonts.googleapis.com/css2?family=Open+Sans:wght@400;600;700&family=Roboto+Condensed:wght@700&display=swap" rel="stylesheet">
<style>
:root{
  --ink:#0d0d0d;
  --panel:#1b1b1b;
  --panel-2:#262626;
  --line:#3a3a3a;
  --white:#ffffff;
  --muted:#b9b9b9;
  --orange:#f26a1b;
  --orange-2:#ff8a2a;
  --red:#d9261c;
  --green:#5fbf2a;
  --lime:#c8e63c;
  --card:#f4f4f4;
}
*{box-sizing:border-box;margin:0;padding:0}
html,body{width:1200px;height:2800px;overflow:hidden;background:var(--ink);font-family:"Open Sans",Arial,sans-serif;color:var(--white)}
.page{position:relative;width:1200px;height:2800px}
h1,h2,h3{font-family:"Roboto Condensed","Arial Narrow",sans-serif;font-weight:700}

/* header */
.site-header{height:60px;background:#111;display:flex;align-items:center;justify-content:space-between;padding:0 120px 0 130px;border-bottom:1px solid #222}
.brand{font-family:"Open Sans",Arial,sans-serif;font-weight:700;font-size:26px;color:var(--white)}
.main-nav{display:flex;align-items:center;gap:0;font-size:12px;font-weight:700}
.main-nav a{color:var(--white);text-decoration:none;padding:0 16px;border-left:1px solid #333}
.main-nav .home{width:34px;height:34px;background:var(--orange);display:flex;align-items:center;justify-content:center;margin-right:8px;border:0;padding:0}

/* hero */
.hero{position:relative;height:580px;background:linear-gradient(100deg,#d9dde0 0%,#b9c2c8 35%,#8c98a3 60%,#c5ccd1 100%)}
.hero .slide-arrow{position:absolute;top:270px;width:30px;height:30px;border-radius:50%;background:rgba(0,0,0,.35);display:flex;align-items:center;justify-content:center}
.hero .prev{left:22px}.hero .next{right:22px}
.promo{position:absolute;left:280px;top:400px;width:640px;height:140px;background:rgba(0,0,0,.82);padding:20px 30px}
.promo h2{font-size:38px;letter-spacing:.5px;background:linear-gradient(#e9f57a,#7cc22a);-webkit-background-clip:text;background-clip:text;color:transparent}
.promo form{display:flex;margin-top:14px}
.promo input{width:300px;height:34px;border:0;padding:0 10px;font-size:13px}
.promo button{height:34px;width:110px;border:0;background:var(--red);color:var(--white);font-weight:700;font-size:14px}
.rate-badge{position:absolute;right:28px;top:16px;text-align:center;font-family:"Roboto Condensed",sans-serif}
.rate-badge .rate{font-size:58px;color:var(--orange-2);line-height:1}
.rate-badge .small{font-size:12px;color:var(--white);letter-spacing:1px}
.rate-badge .month{font-size:36px;color:var(--orange-2);line-height:1}

/* welcome */
.welcome{height:300px;background:linear-gradient(#141414,#1c1c1c);text-align:center;padding-top:50px}
.welcome h1{font-size:36px}
.welcome .lead{color:var(--orange);font-weight:700;font-size:15px;margin:16px auto 0;width:560px;line-height:1.45}
.welcome p.body{color:var(--muted);font-size:12px;width:820px;margin:14px auto 0;line-height:1.6}

/* calculators */
.calculators{height:380px;background:linear-gradient(#2b2b2b,#3d3d3d 50%,#232323);display:flex;justify-content:center;gap:30px;padding-top:20px}
.calc-card{width:280px;height:340px;background:var(--card);border-radius:4px;color:#222;text-align:center;padding:12px 14px;box-shadow:0 6px 14px rgba(0,0,0,.5)}
.calc-card h3{font-size:19px;color:#111}
.calc-card .thumb{height:140px;margin:12px 0 8px}
.calc-card .tag{color:#3b7bbf;font-size:13px;font-weight:600}
.calc-card p{font-size:11px;color:#777;line-height:1.5;margin-top:6px}
.btn-start{display:inline-block;margin-top:12px;background:var(--orange);color:var(--white);font-size:11px;font-weight:700;padding:6px 16px;border-radius:2px}

/* products */
.band{height:60px;background:#000}
.products{height:460px;background:#161616;padding-top:40px}
.products h2{text-align:center;font-size:38px}
.products .sub{text-align:center;color:var(--orange);font-size:13px;margin-top:10px}
.tabs{display:flex;margin:30px 0 0 150px;border-bottom:2px solid var(--line);width:900px;font-size:10px}
.tabs span{padding:7px 10px;background:#222;color:#888;margin-right:2px}
.tabs span.active{background:var(--white);color:#111;font-weight:700}
.product-body{display:flex;gap:24px;margin:22px 0 0 150px;width:900px}
.product-body .thumb{width:310px;height:196px;flex:none;border:3px solid #444}
.product-body p{font-size:12px;color:var(--muted);line-height:1.7}
.btn-more{display:inline-block;margin-top:14px;background:var(--orange);color:var(--white);font-size:11px;font-weight:700;padding:6px 14px}

/* specials */
.specials{height:540px;background:#111;padding-top:40px}
.specials-panel{position:relative;margin:0 auto;width:1020px;height:440px;background:linear-gradient(#2f2f2f,#1e1e1e);border:1px solid #3a3a3a}
.specials-panel .ribbon{position:absolute;left:360px;top:-18px;width:300px;height:48px;background:linear-gradient(#7bd83a,#3e9b1c);text-align:center;font-family:"Roboto Condensed",sans-serif;font-size:30px;line-height:48px;color:var(--white)}
.offers{display:flex;gap:40px;justify-content:center;padding-top:62px}
.offer{width:440px}
.offer .thumb{height:200px;border:4px solid var(--white)}
.offer h3{font-size:24px;margin-top:16px}
.offer p{font-size:11px;color:var(--muted);margin-top:8px;line-height:1.55}

/* partners */
.partners{height:140px;background:linear-gradient(#ffffff,#e4e4e4);display:flex;align-items:center;justify-content:space-around;padding:0 100px}
.partner{display:flex;align-items:center;gap:10px;color:#333;font-weight:700;font-size:22px}
.partner i{width:22px;height:22px;border-radius:50%;background:#9a9a9a}

/* footer */
.site-footer{height:220px;background:#151515;display:flex;gap:120px;padding:36px 0 0 130px}
.site-footer h3{font-size:22px}
.site-footer p{font-size:11px;color:var(--muted);margin-top:10px;line-height:1.6;width:380px}
.site-footer form{display:flex;margin-top:14px}
.site-footer input{width:300px;height:30px;border:0;padding:0 8px;font-size:12px}
.site-footer button{height:30px;width:90px;border:0;background:var(--orange);color:var(--white);font-weight:700;font-size:12px}
.contact{display:grid;grid-template-columns:200px 230px;gap:6px 10px;font-size:11px;color:var(--muted);margin-top:12px}
.copyright{height:20px;background:#000;text-align:center;font-size:9px;color:#777;line-height:20px}
.copyright b{background:var(--orange);color:var(--white);padding:1px 6px;font-weight:600}
</style>
</head>
<body>
<div class="page">
  <header class="site-header">
    <div class="brand">KLR Lending Services</div>
    <nav class="main-nav">
      <a class="home" href="#"><svg width="16" height="16" viewBox="0 0 16 16"><path d="M8 2 1 8h2v6h4v-4h2v4h4V8h2z" fill="#fff"/></svg></a>
      <a href="#">ABOUT US</a><a href="#">SERVICES</a><a href="#">OUR CLIENTS</a><a href="#">PARTNERS</a><a href="#">CONTACT US</a>
    </nav>
  </header>

  <section class="hero" role="img" aria-label="Photo of a smiling couple receiving house keys from a lending adviser">
    <span class="slide-arrow prev"><svg width="12" height="12" viewBox="0 0 12 12"><path d="M8 1 3 6l5 5" stroke="#fff" stroke-width="2" fill="none"/></svg></span>
    <span class="slide-arrow next"><svg width="12" height="12" viewBox="0 0 12 12"><path d="M4 1l5 5-5 5" stroke="#fff" stroke-width="2" fill="none"/></svg></span>
    <div class="promo">
      <h2>INTEREST RATE SPECIAL</h2>
      <form><input type="email" placeholder="Enter your email address"><button type="button">SUBMIT</button></form>
      <div class="rate-badge">
        <div class="rate">4.5%</div>
        <div class="small">FOR THE MONTH OF</div>
        <div class="month">JUNE</div>
      </div>
    </div>
  </section>

  <section class="welcome">
    <h1>Welcome to KLR Lending Services</h1>
    <p class="lead">KLR Lending Services offers a complete range of Mortgage and Loan products to suit our individual clients needs.</p>
    <p class="body">Whether you are a First Home Buyer, Up-Sizing or Down-Sizing, Refinancing, Investing or simply want a new car or equipment purchase, contact us for a no-obligation assessment and get the latest information on the available products to suit your needs.</p>
  </section>

  <section class="calculators">
    <article class="calc-card">
      <h3>Repayment Calculators</h3>
      <div class="thumb" role="img" aria-label="Photo of a hand using a calculator over paperwork" style="background:linear-gradient(135deg,#d9cfb8,#8f8a7c)"></div>
      <div class="tag">Check your loan affordability</div>
      <p>Work out your regular repayments on any loan amount, term and rate in just a few quick steps.</p>
      <span class="btn-start">START</span>
    </article>
    <article class="calc-card">
      <h3>Borrow Capacity Calculators</h3>
      <div class="thumb" role="img" aria-label="Photo of a loan application form with a pen" style="background:linear-gradient(135deg,#e4e6ea,#9aa3ad)"></div>
      <div class="tag">How much can you borrow?</div>
      <p>Enter your income and expenses to see an estimate of how much you may be able to borrow today.</p>
      <span class="btn-start">START</span>
    </article>
    <article class="calc-card">
      <h3>Stamp Duty Calculators</h3>
      <div class="thumb" role="img" aria-label="Illustration of a small house on a stack of coins" style="background:linear-gradient(135deg,#f2d36b,#c9883a)"></div>
      <div class="tag">Get the information you need</div>
      <p>Estimate stamp duty and government fees on your next property purchase before you make an offer.</p>
      <span class="btn-start">START</span>
    </article>
  </section>

  <div class="band"></div>

  <section class="products">
    <h2>Our Products Include</h2>
    <p class="sub">KLR Lending offers a complete range of finance solutions tailored to meet individual client needs.</p>
    <div class="tabs">
      <span class="active">New Homes</span><span>First Home Owners</span><span>Refinance</span><span>Investment</span><span>Mortgage</span><span>Car Loans</span><span>Plant &amp; Equipment</span><span>Insurance</span>
    </div>
    <div class="product-body">
      <div class="thumb" role="img" aria-label="Photo of a modern two-storey apartment building" style="background:linear-gradient(#9ec3e6,#dfe6ea 55%,#8c8f8f)"></div>
      <div>
        <p>Buying a new home is one of the biggest decisions you will make. Our brokers compare loans from a wide panel of lenders to find a package that suits your budget and goals. We handle the paperwork, keep you updated at every stage and help you settle on time with confidence.</p>
        <p>Talk to us about fixed, variable and split loans, offset accounts and features that can save you money over the life of your loan.</p>
        <span class="btn-more">READ MORE</span>
      </div>
    </div>
  </section>

  <section class="specials">
    <div class="specials-panel">
      <div class="ribbon">Special Offer</div>
      <div class="offers">
        <article class="offer">
          <div class="thumb" role="img" aria-label="Photo of a smiling woman holding car keys" style="background:linear-gradient(135deg,#e8d9c6,#8a7560)"></div>
          <h3>Interest Rate Special</h3>
          <p>Lock in a low rate this month and enjoy lower repayments from day one. Conditions apply.</p>
        </article>
        <article class="offer">
          <div class="thumb" role="img" aria-label="Photo of a for sale sign in front of a house" style="background:linear-gradient(135deg,#cfe0ee,#7f8c93)"></div>
          <h3>Current Special Offer</h3>
          <p>No application fee on selected home loans for a limited time. Ask our team for details.</p>
        </article>
      </div>
    </div>
  </section>

  <section class="partners">
    <div class="partner"><i></i>Northvale</div>
    <div class="partner"><i></i>Cobalt Bank</div>
    <div class="partner"><i></i>Redgum</div>
    <div class="partner"><i></i>Alderan</div>
    <div class="partner"><i></i>Quarry Bay</div>
  </section>

  <footer class="site-footer">
    <div>
      <h3>Subscribe Our Newsletters</h3>
      <p>Enter your email below to subscribe to our weekly newsletter and receive our latest specials.</p>
      <form><input type="email" placeholder="Email address"><button type="button">SUBMIT</button></form>
    </div>
    <div>
      <h3>Let's keep in touch</h3>
      <div class="contact">
        <span>28 Example Street, Suite 210</span><span>E-mail: info@klrlending-demo.com.au</span>
        <span>Sample Town NSW 2000</span><span>Phone: 02 9000 0000</span>
        <span>Australia</span><span>www.klrlending-demo.com.au</span>
      </div>
    </div>
  </footer>
  <div class="copyright"><b>Copyright © 2024 klrlending-demo.com.au All Rights Reserved.</b></div>
</div>
</body>
</html>
```